Business Card Design Project

Hello! We need a business card design for a new company opening up in Downtown Dallas called Marbrook Cupcakes. We are a cupcake factory and our primary colors are Harbor Teal and Brown. We want to have a design that can be used for multiple positions (Owner/Operations Manager, Assistant Operations Manager, Decorator, Baker, Corporate Sale Rep, Special Events Rep etc) We would like for it to be double sided. Use the following information in your designs:

Renata Vasquill
Assistant Operations Manager
renata@marbrookcupcakes.example
T555.318.9047

Store Hours:
Mon-Thur 10am-9pm
Fri-Sat 10am-10pm
Sun 12pm-7pm

website: www.marbrookcupcakes.example

Address: 2735 Quarry Ln, Dallas TX 75999

The logo is attached.

Industry/Entity Type

Business

Requirements
Must have
• It must be Harbor Teal and Brown.
Nice to have
• Nice for it to be double sided.
Should not have
• No graphics like a cupcake. Just the word logo.

```html
<!DOCTYPE html>
<html lang="en">
<head>
<meta charset="utf-8">
<title>Marbrook Cupcakes – Business Cards</title>
<link rel="stylesheet" href="https://fonts.googleapis.com/css2?family=Source+Sans+3:wght@400&display=swap">
<style>
  :root {
    --brown: #3e1b0f;
    --teal: #65c6d0;
    --teal-text: #6ccad3;
    --paper: #ffffff;
    --ink-dark: #3e1b0f;
  }
  * { box-sizing: border-box; margin: 0; padding: 0; }
  html, body {
    width: 1200px; height: 787px; overflow: hidden;
    background: var(--paper);
    font-family: "Source Sans 3", "Myriad Pro", Arial, sans-serif;
  }
  .sheet { position: relative; width: 1200px; height: 787px; }
  .card {
    position: absolute; width: 587px; height: 334px;
    border-radius: 24px; overflow: hidden;
  }
  .card--front-light { left: 3px; top: 3px; background: var(--paper); border: 2px solid var(--brown); color: var(--ink-dark); }
  .card--back-brown { left: 611px; top: 1px; background: var(--brown); color: var(--teal-text); }
  .card--front-brown { left: 3px; top: 421px; background: var(--brown); color: var(--teal-text); }
  .card--back-teal { left: 611px; top: 421px; background: var(--teal); color: var(--ink-dark); }

  .contact {
    position: absolute; left: 32px; top: 20px;
    font-size: 14.5px; line-height: 19.5px;
  }
  .hours {
    position: absolute; left: 420px; top: 30px;
    font-size: 14.5px; line-height: 19.5px;
  }
  .wordmark {
    position: absolute; left: 0; right: 0; top: 120px;
    text-align: center; font-size: 50px; font-weight: 400;
    letter-spacing: 0.5px; color: var(--teal);
  }
  .card--front-light .wordmark,
  .card--front-brown .wordmark { left: 60px; }
  .card--back-teal .wordmark { color: var(--brown); }
  .address {
    position: absolute; left: 60px; right: 0; top: 256px;
    text-align: center; font-size: 17px;
  }
  .website {
    position: absolute; left: 0; right: 0; top: 283px;
    text-align: center; font-size: 16px;
  }
</style>
</head>
<body>
<main class="sheet">
  <section class="card card--front-light">
    <div class="contact">
      <p>Renata Vasquill</p>
      <p>Assistant Operations Manager</p>
      <p>renata@marbrookcupcakes.example</p>
      <p>T555.318.9047</p>
    </div>
    <p class="wordmark">Marbrook Cupcakes</p>
    <p class="address">Address: 2735 Quarry Ln, Dallas TX 75999</p>
  </section>

  <section class="card card--back-brown">
    <div class="hours">
      <p>Store Hours:</p>
      <p>Mon-Thur 10am-9pm</p>
      <p>Fri-Sat 10am-10pm</p>
      <p>Sun 12pm-7pm</p>
    </div>
    <p class="wordmark">Marbrook Cupcakes</p>
    <p class="website">website: www.marbrookcupcakes.example</p>
  </section>

  <section class="card card--front-brown">
    <div class="contact">
      <p>Renata Vasquill</p>
      <p>Assistant Operations Manager</p>
      <p>renata@marbrookcupcakes.example</p>
      <p>T555.318.9047</p>
    </div>
    <p class="wordmark">Marbrook Cupcakes</p>
    <p class="address">Address: 2735 Quarry Ln, Dallas TX 75999</p>
  </section>

  <section class="card card--back-teal">
    <div class="hours">
      <p>Store Hours:</p>
      <p>Mon-Thur 10am-9pm</p>
      <p>Fri-Sat 10am-10pm</p>
      <p>Sun 12pm-7pm</p>
    </div>
    <p class="wordmark">Marbrook Cupcakes</p>
    <p class="website">website: www.marbrookcupcakes.example</p>
  </section>
</main>
</body>
</html>
```